Budget planning & tracking app

I want to make personal budget planning and tracking easier and more enjoyable for people from all walks of life. I will aim to assist students, graduates, young professionals and anyone else interested, to get a grip on their personal finances early-on in life, allowing them to build their wealth plan to retirement, and also giving them an easy way to track their financial performance. I want to develop an intuative app that will make capturing daily transaction details a seamless and easy process.

Target Market(s)

This app must appeal to anyone in need of an easy and intuative solution to track their daily finances and to understand what their current lifestyle will mean for their wealth building..

Industry/Entity Type

Personal finance

Font styles to use
Sans Serif

Requirements
Must have
• Super easy and intuative interface, easy capturing of actual expenses, easy setup of planned income and expenses, visual representation of wealth building over time.
Nice to have
• Would be nice if there's.some way to present the solution in a gaming interface, so capturing daily expenses feels less like a chore and more like a game.
Should not have
• Should not look like a spreadsheet.

```html
<!DOCTYPE html>
<html lang="en">
<head>
<meta charset="utf-8">
<title>Budget Planning & Tracking App – Screens</title>
<link href="https://fonts.googleapis.com/css2?family=Manrope:wght@400;500;600;700;800&display=swap" rel="stylesheet">
<style>
  :root{
    --green:#6a9a4a;
    --green-soft:#c9d9ba;
    --green-figure:#b9cfa4;
    --green-text:#eef4e8;
    --figure-text:#ffffff;
    --red:#c0393b;
    --ink:#1f1f1f;
    --muted:#8a8a86;
    --faint:#c8c9c4;
    --bar:#c9cbc5;
    --screen:#f3f3f1;
    --card:#fbfbfa;
    --line:#dcdcd8;
    --white:#ffffff;
  }
  *{box-sizing:border-box;margin:0;padding:0}
  html,body{width:1200px;height:1013px;overflow:hidden;background:var(--white);font-family:'Manrope',sans-serif;color:var(--ink)}
  .board{position:absolute;left:0;top:0;width:2100px;height:1770px;transform:scale(0.5714);transform-origin:0 0}
  .screen{position:absolute;top:165px;width:312px;background:var(--screen);overflow:hidden}
  .abs{position:absolute}

  /* chart header */
  .chart-card{position:absolute;left:0;top:0;width:312px;height:218px;background:var(--card);border-radius:0 0 40px 40px;box-shadow:0 4px 6px rgba(0,0,0,.06)}
  .chart-card.short{height:200px}
  .chart-card.flat{height:235px;border-radius:0}
  .totals{position:absolute;top:14px;left:0;width:312px;text-align:center;font-size:11px;color:var(--muted);white-space:nowrap}
  .totals .f{color:var(--red)}
  .totals svg{vertical-align:-2px;margin-left:6px}
  .spark{position:absolute;left:0;top:0}
  .months{position:absolute;top:190px;left:0;width:312px;height:30px}
  .months span{position:absolute;top:0;font-size:11px;color:var(--faint);transform:translateX(-50%);white-space:nowrap}
  .months span.near{color:var(--muted)}
  .months span.now{color:var(--green);font-weight:700;font-size:13px;top:-1px}
  .months i{position:absolute;left:133px;top:25px;width:50px;height:3px;background:var(--green);border-radius:2px}

  /* tiles */
  .cta{position:absolute;left:21px;top:233px;width:270px;height:51px;border-radius:26px;background:var(--green);color:var(--white);font-weight:700;font-size:14px;display:flex;align-items:center;justify-content:center;box-shadow:0 3px 5px rgba(0,0,0,.15)}
  .tile{position:absolute;width:124px;background:var(--white);border:1.5px solid var(--line);border-radius:12px;display:flex;flex-direction:column;padding:12px 0 0 16px}
  .tile.on{border-color:var(--green)}
  .tile .label{font-size:13px;font-weight:700}
  .tile .value{flex:1;display:flex;align-items:center;justify-content:center;margin-left:-16px;padding-bottom:14px;font-weight:800;font-size:22px;color:var(--faint)}
  .tile.short .value{align-items:flex-start;padding-top:4px}
  .tile .value.big{font-size:34px}
  .value.gain{color:var(--green)}
  .value.loss{color:var(--red)}

  .fab{position:absolute;width:70px;height:70px;border-radius:50%;background:var(--green);display:flex;align-items:center;justify-content:center;box-shadow:0 4px 6px rgba(0,0,0,.2)}

  /* tabs */
  .tabs{position:absolute;left:0;width:312px;height:36px;background:var(--card);border-bottom:1px solid var(--line)}
  .tabs span{position:absolute;top:10px;font-size:11px;color:var(--muted);white-space:nowrap}
  .tabs .active{color:var(--green);font-weight:700;font-size:12px;top:9px}
  .tabs .active::after{content:"";position:absolute;left:0;right:0;bottom:-8px;height:3px;background:var(--green);border-radius:2px}
  .tabs .dim{color:var(--faint)}
  .tabs svg{position:absolute;top:11px}

  .pill{position:absolute;height:34px;border-radius:17px;background:var(--green-soft);font-size:11px;color:var(--green-text);display:flex;align-items:center;padding-left:14px;box-shadow:0 2px 3px rgba(0,0,0,.08)}
  .pill.figure{background:var(--green-figure);color:var(--figure-text);font-weight:600;font-size:11.5px}
  .circle{position:absolute;width:34px;height:34px;border-radius:50%;background:var(--green-soft);display:flex;align-items:center;justify-content:center}

  .entry-head{position:absolute;top:428px;font-size:13px;font-weight:700;color:var(--green)}
  .entry{position:absolute;left:11px;width:288px;height:35px;background:var(--white);border:1.5px solid var(--green);border-radius:6px;font-size:11px}
  .entry span{position:absolute;top:10px}
  .entry .neg{color:var(--red)}

  .month{position:absolute;left:18px;width:32px;font-size:13px;font-weight:700;color:var(--green)}

  /* auto fill */
  .af-title{position:absolute;left:58px;top:16px;font-size:18px;font-weight:700;color:#444}
  .af-row{position:absolute;left:24px;font-size:11px;color:#555;display:flex;align-items:center;gap:8px;white-space:nowrap}
  .chip{width:44px;height:20px;border-radius:10px;background:var(--green-soft);color:var(--green-text);font-size:11px;display:flex;align-items:center;justify-content:center}
  .af-or{position:absolute;left:18px;top:196px;width:278px;height:20px}
  .af-or::before{content:"";position:absolute;left:0;right:0;top:10px;height:1px;background:var(--muted)}
  .af-or span{position:absolute;left:50%;transform:translateX(-50%);background:var(--screen);padding:0 6px;font-size:12px;font-weight:700;color:#555;top:1px}
  .apply{position:absolute;left:187px;top:596px;width:109px;height:28px;border-radius:14px;background:var(--green);color:var(--white);font-weight:700;font-size:13px;display:flex;align-items:center;justify-content:center;box-shadow:0 2px 4px rgba(0,0,0,.15)}

  /* summary */
  .col-head{position:absolute;top:244px;font-size:13px;font-weight:600;transform:translateX(-50%)}
  .line-name{position:absolute;left:10px;font-size:11px;font-weight:700;line-height:1}
</style>
</head>
<body>
<svg width="0" height="0" style="position:absolute" aria-hidden="true">
  <symbol id="spark" viewBox="0 0 312 200">
    <g stroke-linecap="round" stroke-width="7" fill="none">
      <line x1="28" y1="80" x2="28" y2="120" stroke="#c9cbc5"/>
      <line x1="40" y1="67" x2="40" y2="120" stroke="#6a9a4a"/>
      <line x1="52" y1="87" x2="52" y2="120" stroke="#c9cbc5"/>
      <line x1="64" y1="124" x2="64" y2="173" stroke="#c0393b"/>
      <line x1="76" y1="124" x2="76" y2="168" stroke="#c0393b"/>
      <line x1="88" y1="124" x2="88" y2="153" stroke="#c0393b"/>
      <line x1="100" y1="124" x2="100" y2="138" stroke="#c0393b"/>
      <line x1="113" y1="92" x2="113" y2="120" stroke="#c9cbc5"/>
      <line x1="125" y1="79" x2="125" y2="120" stroke="#c9cbc5"/>
      <line x1="137" y1="87" x2="137" y2="120" stroke="#c9cbc5"/>
      <line x1="149" y1="99" x2="149" y2="120" stroke="#c9cbc5"/>
      <line x1="161" y1="92" x2="161" y2="120" stroke="#c9cbc5"/>
      <line x1="174" y1="112" x2="174" y2="120" stroke="#c9cbc5"/>
      <line x1="186" y1="85" x2="186" y2="120" stroke="#c9cbc5"/>
      <line x1="198" y1="99" x2="198" y2="120" stroke="#c9cbc5"/>
      <line x1="210" y1="102" x2="210" y2="120" stroke="#c9cbc5"/>
      <line x1="222" y1="99" x2="222" y2="120" stroke="#c9cbc5"/>
      <line x1="234" y1="89" x2="234" y2="120" stroke="#c9cbc5"/>
      <line x1="247" y1="82" x2="247" y2="120" stroke="#c9cbc5"/>
      <line x1="259" y1="79" x2="259" y2="120" stroke="#c9cbc5"/>
      <line x1="271" y1="99" x2="271" y2="120" stroke="#c9cbc5"/>
      <line x1="283" y1="69" x2="283" y2="120" stroke="#c9cbc5"/>
    </g>
  </symbol>
  <symbol id="cal" viewBox="0 0 14 14"><rect x="1" y="2" width="12" height="11" rx="1.5" fill="none" stroke="#8a8a86"/><path d="M1 5.5h12M4 8h2M8 8h2M4 10.5h2" stroke="#8a8a86"/></symbol>
  <symbol id="back" viewBox="0 0 40 40"><path d="M34 20H8M18 9 7 20l11 11" fill="none" stroke="#fff" stroke-width="4" stroke-linecap="round" stroke-linejoin="round"/></symbol>
  <symbol id="home" viewBox="0 0 40 40"><path d="M20 6 6 17v17h10v-9h8v9h10V17z" fill="#fff"/></symbol>
  <symbol id="arrow" viewBox="0 0 22 12"><path d="M21 6H2M7 1 1.5 6 7 11" fill="none" stroke="#8a8a86" stroke-width="1.5" stroke-linecap="round"/></symbol>
</svg>

<main class="board">

  <!-- Screen 1: category overview -->
  <section class="screen" style="left:115px;height:1435px">
    <div class="chart-card">
      <p class="totals">P: 149, 584 &nbsp;&nbsp;A: 143, 221 &nbsp;&nbsp;<span class="f">F: 159, 003</span><svg width="14" height="14"><use href="#cal"/></svg></p>
      <svg class="spark" width="312" height="200"><use href="#spark"/></svg>
      <div class="months"><span style="left:35px">SEP 23</span><span class="near" style="left:93px">SEP 23</span><span class="now" style="left:155px">SEP 23</span><span class="near" style="left:216px">SEP 23</span><span style="left:275px">SEP 23</span><i></i></div>
    </div>
    <div class="cta">View All</div>

    <div class="tile on short" style="left:21px;top:311px;height:85px"><span class="label">Income</span><span class="value gain">+ 1,600</span></div>
    <div class="tile on short" style="left:21px;top:417px;height:85px"><span class="label">Food</span><span class="value loss">+ 435</span></div>
    <div class="tile on short" style="left:21px;top:524px;height:85px"><span class="label">Unplanned</span><span class="value loss">+ 965</span></div>
    <div class="tile" style="left:21px;top:630px;height:156px"><span class="label">Family</span><span class="value big">0</span></div>
    <div class="tile short" style="left:21px;top:808px;height:85px"><span class="label">Education</span><span class="value">0</span></div>
    <div class="tile short" style="left:21px;top:915px;height:85px"><span class="label">Government</span><span class="value">0</span></div>
    <div class="tile short" style="left:21px;top:1021px;height:85px"><span class="label">Insurance</span><span class="value">0</span></div>
    <div class="tile short" style="left:21px;top:1128px;height:85px"><span class="label">Holidays</span><span class="value">0</span></div>

    <div class="tile" style="left:167px;top:311px;height:156px"><span class="label">Income</span><span class="value big">0</span></div>
    <div class="tile on short" style="left:167px;top:488px;height:85px"><span class="label">Transport</span><span class="value loss">-565</span></div>
    <div class="tile on" style="left:167px;top:595px;height:156px"><span class="label">Bills</span><span class="value big gain">-498</span></div>
    <div class="tile short" style="left:167px;top:772px;height:85px"><span class="label">Loans</span><span class="value">0</span></div>
    <div class="tile on" style="left:167px;top:879px;height:156px"><span class="label">Medical</span><span class="value loss">+1,543</span></div>
    <div class="tile on short" style="left:167px;top:1057px;height:85px"><span class="label">Celebrations</span><span class="value loss">+600</span></div>
    <div class="tile" style="left:167px;top:1163px;height:156px"><span class="label">Housing</span><span class="value big">0</span></div>

    <div class="fab" style="left:221px;top:1340px"><svg width="36" height="28" viewBox="0 0 36 28"><path d="M3 4h30M3 14h30M3 24h30" stroke="#fff" stroke-width="4" stroke-linecap="round"/></svg></div>
  </section>

  <!-- Screen 2: category entries -->
  <section class="screen" style="left:503px;height:855px">
    <div class="chart-card flat">
      <p class="totals">P: 149, 584 &nbsp;&nbsp;A: 143, 221 &nbsp;&nbsp;<span class="f">F: 159, 003</span><svg width="14" height="14"><use href="#cal"/></svg></p>
      <svg class="spark" width="312" height="200"><use href="#spark"/></svg>
      <div class="months"><span style="left:35px">SEP 23</span><span class="near" style="left:93px">SEP 23</span><span class="now" style="left:155px">SEP 23</span><span class="near" style="left:216px">SEP 23</span><span style="left:275px">SEP 23</span><i></i></div>
    </div>
    <nav class="tabs" style="top:237px"><svg width="22" height="12" style="left:61px"><use href="#arrow"/></svg><span class="active" style="left:105px">Grocery</span><span style="left:177px">Fast Food</span><span class="dim" style="left:252px">Dine Out</span></nav>
    <p class="abs" style="top:284px;left:0;width:312px;text-align:center;font-size:11px;color:var(--muted)">✎ &nbsp;P: 1,174 &nbsp;&nbsp;<span style="color:var(--red)">A: 1,938 &nbsp;&nbsp;F: 2,041</span></p>
    <div class="circle" style="left:11px;top:320px"><svg width="14" height="4"><path d="M1 2h12" stroke="#6a9a4a" stroke-width="2.5" stroke-linecap="round"/></svg></div>
    <div class="pill" style="left:50px;top:320px;width:210px">Enter Value</div>
    <div class="circle" style="left:266px;top:320px"><svg width="16" height="16"><path d="M1 8h14M8 1v14" stroke="#6a9a4a" stroke-width="2.5" stroke-linecap="round"/></svg></div>
    <div class="pill" style="left:11px;top:368px;width:288px">Notes</div>

    <span class="entry-head" style="left:29px">Date</span>
    <span class="entry-head" style="left:87px">Value</span>
    <span class="entry-head" style="left:150px">Note</span>

    <div class="entry" style="top:457px"><span style="left:16px">Aug 15</span><span style="left:80px">15.50</span><span style="left:144px">Lunch</span></div>
    <div class="entry" style="top:506px"><span style="left:16px">Aug 14</span><span style="left:80px">195.67</span><span style="left:144px">Groceries</span></div>
    <div class="entry" style="top:556px"><span style="left:16px">Aug 7</span><span style="left:80px">5.45</span><span style="left:144px">QuickMart</span></div>
    <div class="entry" style="top:605px"><span style="left:16px">Aug 3</span><span style="left:80px">234.53</span><span style="left:144px">-</span></div>
    <div class="entry" style="top:655px"><span style="left:16px">Aug 1</span><span class="neg" style="left:75px">-100.00</span><span style="left:139px">Refund</span></div>
    <div class="entry" style="top:704px"><span style="left:16px">Aug 1</span><span style="left:80px">234.50</span><span style="left:144px">-</span></div>

    <div class="fab" style="left:20px;top:760px"><svg width="44" height="44"><use href="#back"/></svg></div>
    <div class="fab" style="left:221px;top:760px"><svg width="38" height="38"><use href="#home"/></svg></div>
  </section>

  <!-- Screen 3: budget planning -->
  <section class="screen" style="left:890px;height:1057px">
    <div class="chart-card short">
      <p class="totals">P: 149, 584 &nbsp;&nbsp;A: 143, 221 &nbsp;&nbsp;<span class="f">F: 159, 003</span><svg width="14" height="14"><use href="#cal"/></svg></p>
      <svg class="spark" width="312" height="200"><use href="#spark"/></svg>
    </div>
    <nav class="tabs" style="top:216px"><svg width="22" height="12" style="left:61px"><use href="#arrow"/></svg><span class="active" style="left:105px">Grocery</span><span style="left:177px">Fast Food</span><span class="dim" style="left:252px">Dine Out</span></nav>
    <p class="abs" style="top:263px;left:74px;font-size:13px;font-weight:600;display:flex;align-items:center;gap:14px">
      <svg width="16" height="16" viewBox="0 0 16 16"><g fill="none" stroke="#6a9a4a" stroke-width="1.3"><rect x="1" y="1" width="5.5" height="5.5"/><rect x="9.5" y="1" width="5.5" height="5.5"/><rect x="1" y="9.5" width="5.5" height="5.5"/><rect x="9.5" y="9.5" width="5.5" height="5.5"/></g></svg>
      Budget Planning
      <svg width="16" height="16" viewBox="0 0 16 16"><path d="M2 14 12 3l2 2L4 15zM2 14l1-4" fill="none" stroke="#6a9a4a" stroke-width="1.3"/></svg>
    </p>
    <span class="abs" style="top:302px;left:18px;font-size:13px;font-weight:700;color:var(--green)">2023</span>

    <span class="month" style="top:330px">JAN</span><div class="pill" style="left:56px;top:321px;width:110px">Value</div><div class="pill" style="left:173px;top:321px;width:132px">Notes</div>
    <span class="month" style="top:379px">FEB</span><div class="pill" style="left:56px;top:370px;width:110px">Value</div><div class="pill" style="left:173px;top:370px;width:132px">Notes</div>
    <span class="month" style="top:428px">MAR</span><div class="pill" style="left:56px;top:418px;width:110px">Value</div><div class="pill" style="left:173px;top:418px;width:132px">Notes</div>
    <span class="month" style="top:476px">APR</span><div class="pill" style="left:56px;top:467px;width:110px">Value</div><div class="pill" style="left:173px;top:467px;width:132px">Notes</div>
    <span class="month" style="top:525px">MAY</span><div class="pill" style="left:56px;top:516px;width:110px">Value</div><div class="pill" style="left:173px;top:516px;width:132px">Notes</div>
    <span class="month" style="top:573px">JUN</span><div class="pill" style="left:56px;top:564px;width:110px">Value</div><div class="pill" style="left:173px;top:564px;width:132px">Notes</div>
    <span class="month" style="top:622px">JUL</span><div class="pill" style="left:56px;top:613px;width:110px">Value</div><div class="pill" style="left:173px;top:613px;width:132px">Notes</div>
    <span class="month" style="top:670px">AUG</span><div class="pill" style="left:56px;top:661px;width:110px">Value</div><div class="pill" style="left:173px;top:661px;width:132px">Notes</div>
    <span class="month" style="top:719px">SEP</span><div class="pill" style="left:56px;top:710px;width:110px">Value</div><div class="pill" style="left:173px;top:710px;width:132px">Notes</div>
    <span class="month" style="top:767px">OCT</span><div class="pill" style="left:56px;top:758px;width:110px">Value</div><div class="pill" style="left:173px;top:758px;width:132px">Notes</div>
    <span class="month" style="top:816px">NOV</span><div class="pill" style="left:56px;top:807px;width:110px">Value</div><div class="pill" style="left:173px;top:807px;width:132px">Notes</div>
    <span class="month" style="top:864px">DEC</span><div class="pill" style="left:56px;top:855px;width:110px">Value</div><div class="pill" style="left:173px;top:855px;width:132px">Notes</div>
    <span class="month" style="top:913px;left:16px">YEAR</span><div class="pill" style="left:56px;top:904px;width:110px">Value<svg width="12" height="8" style="position:absolute;right:12px;top:13px"><path d="M1 1l5 5 5-5" fill="none" stroke="#6a9a4a" stroke-width="2"/></svg></div>

    <div class="fab" style="left:20px;top:963px"><svg width="44" height="44"><use href="#back"/></svg></div>
    <div class="fab" style="left:221px;top:963px"><svg width="38" height="38"><use href="#home"/></svg></div>
  </section>

  <!-- Screen 4: auto fill -->
  <section class="screen" style="left:1278px;height:645px">
    <svg class="abs" width="22" height="14" style="left:18px;top:19px" viewBox="0 0 22 12"><path d="M21 6H2M7 1 1.5 6 7 11" fill="none" stroke="#444" stroke-width="2" stroke-linecap="round"/></svg>
    <h1 class="af-title">Auto Fill</h1>
    <p class="af-row" style="top:82px">Repeat every <span class="chip">0</span> month(s)</p>
    <p class="af-row" style="top:117px">For next <span class="chip">0</span> year(s) and escalate</p>
    <p class="af-row" style="top:151px">With <span class="chip">0</span> % per year.</p>
    <div class="af-or"><span>Or</span></div>
    <p class="af-row" style="top:235px">Repeat previous year's values</p>
    <p class="af-row" style="top:268px">For next <span class="chip">0</span> year(s) and escalate</p>
    <p class="af-row" style="top:303px">With <span class="chip">0</span> % per year.</p>
    <div class="apply">Apply</div>
  </section>

  <!-- Screen 5: planned vs actual -->
  <section class="screen" style="left:1665px;height:893px">
    <div class="chart-card">
      <p class="totals">P: 149, 584 &nbsp;&nbsp;A: 143, 221 &nbsp;&nbsp;<span class="f">F: 159, 003</span><svg width="14" height="14"><use href="#cal"/></svg></p>
      <svg class="spark" width="312" height="200"><use href="#spark"/></svg>
      <div class="months"><span style="left:35px">SEP 23</span><span class="near" style="left:93px">SEP 23</span><span class="now" style="left:155px">SEP 23</span><span class="near" style="left:216px">SEP 23</span><span style="left:275px">SEP 23</span><i></i></div>
    </div>
    <span class="col-head" style="left:155px">Planned</span>
    <span class="col-head" style="left:256px">Actual</span>

    <span class="line-name" style="top:281px">Net</span><div class="pill figure" style="left:111px;top:270px;width:88px">23,659</div><div class="pill figure" style="left:213px;top:270px;width:88px">24,588</div>
    <span class="line-name" style="top:329px">Income</span><div class="pill figure" style="left:111px;top:317px;width:88px">97,507</div><div class="pill figure" style="left:213px;top:317px;width:88px">101,509</div>
    <span class="line-name" style="top:377px">Salary</span><div class="pill figure" style="left:111px;top:365px;width:88px">86,535</div><div class="pill figure" style="left:213px;top:365px;width:88px">90,510</div>
    <span class="line-name" style="top:424px">Basic</span><div class="pill figure" style="left:111px;top:412px;width:88px">0.00</div><div class="pill figure" style="left:213px;top:412px;width:88px">0.00</div>
    <span class="line-name" style="top:466px">Housing<br>Allowance</span><div class="pill figure" style="left:111px;top:460px;width:88px">0.00</div><div class="pill figure" style="left:213px;top:460px;width:88px">0.00</div>
    <span class="line-name" style="top:514px">Housing<br>Recovery</span><div class="pill figure" style="left:111px;top:508px;width:88px">677</div><div class="pill figure" style="left:213px;top:508px;width:88px">0.00</div>
    <span class="line-name" style="top:567px">Schooling</span><div class="pill figure" style="left:111px;top:555px;width:88px">0.00</div><div class="pill figure" style="left:213px;top:555px;width:88px">0.00</div>
    <span class="line-name" style="top:615px">Travel</span><div class="pill figure" style="left:111px;top:603px;width:88px">0.00</div><div class="pill figure" style="left:213px;top:603px;width:88px">0.00</div>
    <span class="line-name" style="top:663px">Reimbursement</span><div class="pill figure" style="left:111px;top:651px;width:88px">0.00</div><div class="pill figure" style="left:213px;top:651px;width:88px">0.00</div>
    <span class="line-name" style="top:710px">Bonus</span><div class="pill figure" style="left:111px;top:698px;width:88px">0.00</div><div class="pill figure" style="left:213px;top:698px;width:88px">0.00</div>
    <span class="line-name" style="top:758px">Other Funds</span><div class="pill figure" style="left:111px;top:746px;width:88px">10,973</div><div class="pill figure" style="left:213px;top:746px;width:88px">10,999</div>

    <div class="fab" style="left:20px;top:800px"><svg width="44" height="44"><use href="#back"/></svg></div>
    <div class="fab" style="left:221px;top:800px"><svg width="38" height="38"><use href="#home"/></svg></div>
  </section>

</main>
</body>
</html>
```